Freelance business trainer needs a new business card

My business is called Tbrite. I provide training in the workplace on management, coaching and mentoring, and customer service topics for a variety of businesses, colleges and private training providers, and teach on management programs. I need a professional but eye catching business card. Business colours grey and orange. My name Linda Marchbank; Tel 07853 416207; email lmarchbank@tbrite.co.uk; website www.tbrite.co.uk.
Happy to have some sort of logo on front and details on back or all on one side
Target Market(s)
SME businesses and colleges - workshops i run are for adults in the workplace
Industry/Entity Type
Training
Look and feel

```html
<!DOCTYPE html>
<html lang="en">
<head>
<meta charset="utf-8">
<title>Tbrite business card</title>
<link href="https://fonts.googleapis.com/css2?family=Arimo:wght@400;700&display=swap" rel="stylesheet">
<style>
  :root {
    --orange: #f7901e;
    --orange-soft: #f9a54a;
    --grey: #7d7d7d;
    --grey-dark: #5a5a5a;
    --grey-band: #858585;
    --white: #ffffff;
    --paper: #f7f7f7;
    --backdrop: #e4e4e4;
  }
  * { box-sizing: border-box; margin: 0; padding: 0; }
  html, body {
    width: 1200px; height: 1000px; overflow: hidden;
    background: var(--backdrop);
    font-family: "Arimo", Arial, sans-serif;
  }
  .sheet {
    width: 1200px; height: 1000px;
    display: flex; justify-content: center; align-items: center; gap: 120px;
  }
  .card {
    width: 340px; height: 530px;
    position: relative; overflow: hidden;
    box-shadow: 0 6px 18px rgba(0,0,0,0.18);
  }
  /* Front */
  .card-front { background: var(--orange); }
  .front-illustration {
    position: absolute; left: 90px; top: 70px;
    width: 160px; height: 190px;
    border-radius: 80px 80px 40px 40px;
    background: radial-gradient(circle at 50% 40%, #a08a74 0%, var(--orange) 75%);
    opacity: 0.8;
  }
  .front-website {
    position: absolute; left: 0; right: 0; bottom: 70px;
    text-align: center; color: var(--grey);
    font-size: 27px; font-weight: 700; letter-spacing: 0.5px;
  }
  /* Back */
  .card-back { background: var(--paper); }
  .back-header {
    height: 150px; background: var(--grey-band);
    padding: 18px 20px;
  }
  .logo-plate {
    height: 114px; background: var(--white); border-radius: 12px;
    display: flex; align-items: center; justify-content: center;
  }
  .logo-name {
    color: var(--grey-dark); font-size: 62px; font-weight: 700; letter-spacing: 1px;
  }
  .name-band {
    height: 48px; background: var(--orange);
    color: var(--white); font-size: 27px;
    display: flex; align-items: center; justify-content: center;
  }
  .contact {
    display: flex; flex-direction: column; align-items: center;
    color: var(--grey-dark);
  }
  .contact-phone { margin-top: 34px; }
  .contact-icon { display: block; }
  .contact-text { font-size: 22px; letter-spacing: 1px; margin-top: 14px; }
  .divider {
    width: 200px; height: 1px; background: var(--orange-soft);
    margin: 22px auto 0;
  }
  .contact-email { margin-top: 26px; }
  .contact-email .contact-text { font-size: 20px; letter-spacing: 0; margin-top: 30px; }
</style>
</head>
<body>
<main class="sheet">
  <section class="card card-front" aria-label="Card front">
    <div class="front-illustration" role="img" aria-label="Illustration of a light bulb combined with a head profile, drawn in grey line art"></div>
    <p class="front-website">www.tbrite.co.uk</p>
  </section>

  <section class="card card-back" aria-label="Card back">
    <header class="back-header">
      <div class="logo-plate"><span class="logo-name">Tbrite</span></div>
    </header>
    <div class="name-band">Linda Marchbank</div>

    <div class="contact contact-phone">
      <svg class="contact-icon" width="44" height="30" viewBox="0 0 44 30" aria-hidden="true">
        <path d="M4 12 C10 2, 34 2, 40 12 L40 18 L31 18 L30 12 C26 10, 18 10, 14 12 L13 18 L4 18 Z" fill="var(--orange)"/>
      </svg>
      <span class="contact-text">07853 416207</span>
    </div>

    <div class="divider"></div>

    <div class="contact contact-email">
      <svg class="contact-icon" width="70" height="46" viewBox="0 0 70 46" aria-hidden="true">
        <rect x="0" y="0" width="70" height="46" rx="3" fill="var(--orange)"/>
        <path d="M3 3 L35 26 L67 3" fill="none" stroke="var(--white)" stroke-width="3"/>
        <path d="M3 43 L26 20 M67 43 L44 20" fill="none" stroke="var(--white)" stroke-width="3"/>
      </svg>
      <span class="contact-text">lmarchbank@tbrite.co.uk</span>
    </div>
  </section>
</main>
</body>
</html>
```